Seeking a beautiful packaging box for Dusk Haven - an essential oil blend (mock up provided!)

My sleep brand - Dusk Haven - is almost ready to go to market. And I need a box! Dusk Haven is a high end essential oils/sleep hygiene brand.

I need a gorgeous, classy box for our 3 sizes of essential oil product we are selling. I have a draft mockup which is to approximate size (attached), but need some help with the finishing touches and layout so it's really polished. I am looking for simple/monochrome designs using black and off white (think Norvel inspo!)

We are selling a 15mL dropper bottle and two roll ons (5ml, 10ml) of the essential oil blend. These are all amber bottles with black top. The box design will be almost identical for each, with very slight variations due to size differences.

The size of the boxes will be
15mL dropper: 30x30x95mm
10ml roller: 19x19x88mm
5ml roller: 18x18x59mm

Target Market(s)

High end/high price point product, shift workers, mums, people suffering stress and insomnia

Industry/Entity Type

Health And Wellness

Font styles to use
Serif
Sans Serif

Colors

Designer to choose only greyscale colors for use in the design.

Requirements
Must have
• I have attached a word document which includes all the necessary text:
- ingredients
- directions
- cautions
- info on essential oils/dusk haven (abbreviated on the smallest box)

Additionally:
- volume
- our website
- instagram logo/duskhavenau name
- made in australia
- recycle symbol
- 12 month open symbol
Nice to have
• I would like the boxes to be monochromatic: white or off white colour, with black logo and writing. I am open to variations on the logo (ie position of writing in relation to the circle/change of font size), but mostly need help with layout, font, direction of text, design of the blank spaces, patterns etc.
Should not have
• Colours

```html
<!DOCTYPE html>
<html lang="en">
<head>
<meta charset="utf-8">
<title>Dusk Haven – Essential Oil Blend Box Dielines</title>
<link rel="stylesheet" href="https://fonts.googleapis.com/css2?family=Josefin+Sans:wght@300;400&family=Roboto:wght@400;700&display=swap">
<style>
  :root {
    --backdrop: #f6caa9;
    --paper: #ffffff;
    --ink: #111111;
    --fold: #e4e4e4;
    --wave-line: #9a9a9a;
    --reverse: #ffffff;
  }
  * { box-sizing: border-box; margin: 0; padding: 0; }
  html, body { width: 992px; height: 1200px; overflow: hidden; }
  body {
    background: var(--backdrop);
    position: relative;
    font-family: "Roboto", Arial, sans-serif;
    color: var(--ink);
  }
  .dieline {
    position: absolute;
    background: var(--paper);
    overflow: hidden;
    box-shadow: 0 1px 3px rgba(0,0,0,.12);
  }
  .dieline--dropper { left: 532px; top: 138px; width: 404px; height: 318px; }
  .dieline--roller  { left: 228px; top: 728px; width: 310px; height: 359px; }

  .panel {
    position: absolute; top: 0; height: 100%;
    border-left: 1px solid var(--fold);
  }
  .panel:first-of-type { border-left: none; }

  .band { position: absolute; left: 0; width: 100%; }
  .dieline--dropper .band { top: 250px; height: 68px; }
  .dieline--roller .band { top: 292px; height: 67px; }

  .copy {
    position: absolute; left: 6px; right: 6px;
    text-align: center; font-size: 5.6px; line-height: 7.1px;
  }
  .copy p + p { margin-top: 6px; }
  .rule {
    display: block; width: 11px; height: 2px; background: var(--ink);
    margin: 0 auto 3px;
  }
  .heading { font-weight: 700; font-size: 5.6px; letter-spacing: .1px; }
  .section + .section { margin-top: 9px; }
  .benefits b { font-weight: 700; }

  .brand { position: absolute; left: 0; width: 100%; text-align: center; }
  .brand__circle {
    display: block; margin: 0 auto;
    border: 2px solid var(--ink); border-radius: 50%;
  }
  .brand__name {
    font-family: "Josefin Sans", Arial, sans-serif; font-weight: 300;
    line-height: 1; white-space: nowrap;
  }
  .brand__name span { display: block; }
  .product-name {
    position: absolute; left: 0; width: 100%; text-align: center;
    font-family: "Josefin Sans", Arial, sans-serif; font-weight: 300;
  }

  .reverse {
    position: absolute; color: var(--reverse); text-align: center;
  }
  .reverse--label { font-family: "Josefin Sans", Arial, sans-serif; font-weight: 400; }
  .reverse--small { font-size: 5px; line-height: 6px; text-align: left; }
  .reverse--small b { font-weight: 700; }

  .ingredients-vertical {
    position: absolute; font-size: 5.6px; line-height: 7px;
    transform: rotate(-90deg); transform-origin: center;
    text-align: left;
  }
  .ingredients-vertical .heading { display: flex; align-items: center; gap: 4px; margin-bottom: 1px; }
  .ingredients-vertical .heading::before {
    content: ""; width: 11px; height: 2px; background: var(--ink);
  }
</style>
</head>
<body>

<!-- 15mL dropper box -->
<section class="dieline dieline--dropper" aria-label="Dusk Haven 15mL dropper box dieline">
  <svg class="band" viewBox="0 0 404 68" preserveAspectRatio="none" aria-hidden="true">
    <path d="M0 7 q12.6 -6 25.25 0 t25.25 0 t25.25 0 t25.25 0 t25.25 0 t25.25 0 t25.25 0 t25.25 0 t25.25 0 t25.25 0 t25.25 0 t25.25 0 t25.25 0 t25.25 0 t25.25 0 t25.25 0" fill="none" stroke="var(--wave-line)" stroke-width="1"/>
    <path d="M0 11 q12.6 -6 25.25 0 t25.25 0 t25.25 0 t25.25 0 t25.25 0 t25.25 0 t25.25 0 t25.25 0 t25.25 0 t25.25 0 t25.25 0 t25.25 0 t25.25 0 t25.25 0 t25.25 0 t25.25 0 V68 H0 Z" fill="var(--ink)"/>
  </svg>

  <div class="panel" style="left:0;width:101px;">
    <div class="copy" style="top:62px;">
      <span class="rule"></span>
      <p class="heading">INGREDIENTS:</p>
      <p style="margin-top:3px;">Lavandula Angustifolia (Australian Lavender), Vetiveria Zizanoides (Vetiver) Root Oil, Sweet Vanilla Fragrant Oil, Pelargonium Capitatum (Cape Rose Geranium) Leaf Extract, Juniperus Virginiana (Cedarwood) Wood Oil, Citrus Limon (Australian Lemon) Peel Oil, Origanum Majorana (Marjoram) Leaf Oil, Cananga Odorata (Ylang Ylang) Flower Oil, Anthemis Nobilis (Roman Chamomile) Flower Oil</p>
    </div>
  </div>

  <div class="panel" style="left:101px;width:101px;">
    <div class="brand" style="top:60px;">
      <span class="brand__circle" style="width:50px;height:50px;"></span>
      <p class="brand__name" style="margin-top:12px;">
        <span style="font-size:19px;letter-spacing:2.5px;">DUSK</span>
        <span style="font-size:8px;letter-spacing:5px;margin-top:3px;padding-left:5px;">HAVEN</span>
      </p>
    </div>
    <p class="product-name" style="top:235px;font-size:6.8px;letter-spacing:.3px;">ESSENTIAL OIL BLEND</p>
    <p class="reverse reverse--label" style="left:0;width:100%;top:276px;font-size:5.8px;">Made in Australia</p>
    <p class="reverse reverse--label" style="left:0;width:100%;top:294px;font-size:5.8px;">15mL</p>
  </div>

  <div class="panel" style="left:202px;width:101px;">
    <div class="copy" style="top:62px;">
      <div class="section"><span class="rule"></span><p class="heading">DIFFUSE</p><p style="margin-top:0;">Add 4-6 drops to a diffuser or oil burner at night to create a calm and grounded environment.</p></div>
      <div class="section"><span class="rule"></span><p class="heading">BATHE</p><p style="margin-top:0;">Add 2-4 drops to a warm bath to help calm the body and mind</p></div>
      <div class="section"><span class="rule"></span><p class="heading">INHALE</p><p style="margin-top:0;">Place 2 drops in the palms of the hands and inhale directly to ease you into a restful sleep</p></div>
      <div class="section"><span class="rule"></span><p class="heading">MASSAGE</p><p style="margin-top:0;">Dilute 4 drops with a carrier oil (such as jojoba or coconut), and massage into the feet before sleep</p></div>
    </div>
    <p class="reverse reverse--small" style="left:9px;right:6px;top:274px;"><b>CAUTION:</b><br>Possible skin sensitivity. Keep out of reach of children. Not for ingestion or internal use. Avoid contact with eyes, inner ears and sensitive areas.</p>
  </div>

  <div class="panel" style="left:303px;width:101px;">
    <div class="copy benefits" style="top:62px;">
      <span class="rule"></span>
      <p>Essential Oils have been used for centuries to help prepare the mind and body for sleep</p>
      <p>Dusk Haven contain a balanced blend of the most sleep supporting essential oils, renowned for their grounding and calming properties.</p>
      <p><b>Lavender</b> for restfulness<br><b>Vetiver</b> for grounding<br><b>Cedarwood</b> for relaxation<br><b>Marjoram</b> for balance<br><b>Roman Chamomile</b> for comfort</p>
      <p>Add Dusk Haven to your nightly bedtime ritual to help support you in achieving deep and rejuvenating sleep</p>
    </div>
    <p class="reverse reverse--small" style="left:10px;right:4px;top:275px;"><b>Visit</b> www.duskhaven.com.au<br>to learn more</p>
    <p class="reverse reverse--small" style="left:10px;right:4px;top:294px;">IG @duskhavenau</p>
  </div>
</section>

<!-- Roll-on box -->
<section class="dieline dieline--roller" aria-label="Dusk Haven roll on box dieline">
  <svg class="band" viewBox="0 0 310 67" preserveAspectRatio="none" aria-hidden="true">
    <path d="M0 7 q9.7 -6 19.4 0 t19.4 0 t19.4 0 t19.4 0 t19.4 0 t19.4 0 t19.4 0 t19.4 0 t19.4 0 t19.4 0 t19.4 0 t19.4 0 t19.4 0 t19.4 0 t19.4 0 t19.4 0" fill="none" stroke="var(--wave-line)" stroke-width="1"/>
    <path d="M0 11 q9.7 -6 19.4 0 t19.4 0 t19.4 0 t19.4 0 t19.4 0 t19.4 0 t19.4 0 t19.4 0 t19.4 0 t19.4 0 t19.4 0 t19.4 0 t19.4 0 t19.4 0 t19.4 0 t19.4 0 V67 H0 Z" fill="var(--ink)"/>
  </svg>

  <div class="panel" style="left:0;width:77.5px;">
    <div class="ingredients-vertical" style="width:236px;height:48px;left:-79px;top:139px;">
      <p class="heading">INGREDIENTS:</p>
      <p>Lavandula Angustifolia (Australian Lavender), Vetiveria Zizanoides (Vetiver) Root Oil, Sweet Vanilla Fragrant Oil, Pelargonium Capitatum (Cape Rose Geranium) Leaf Extract, Juniperus Virginiana (Cedarwood) Wood Oil, Citrus Limon (Australian Lemon) Peel Oil, Origanum Majorana (Marjoram) Leaf Oil, Cananga Odorata (Ylang Ylang) Flower Oil, Anthemis Nobilis (Roman Chamomile) Flower Oil</p>
    </div>
  </div>

  <div class="panel" style="left:77.5px;width:77.5px;">
    <div class="brand" style="top:93px;">
      <span class="brand__circle" style="width:44px;height:44px;"></span>
      <p class="brand__name" style="margin-top:12px;">
        <span style="font-size:16px;letter-spacing:2px;">DUSK</span>
        <span style="font-size:7px;letter-spacing:4px;margin-top:3px;padding-left:4px;">HAVEN</span>
      </p>
    </div>
    <p class="product-name" style="top:236px;font-size:8px;line-height:12px;letter-spacing:.4px;">ROLL ON<br>ESSENTIAL<br>OIL BLEND</p>
  </div>

  <div class="panel" style="left:155px;width:77.5px;">
    <div class="copy" style="top:42px;left:4px;right:4px;">
      <span class="rule"></span>
      <p class="heading">DIRECTIONS:</p>
      <p style="margin-top:0;">Apply directly on to skin. For sensitive skin, dilute with a carrier oil (such as jojoba or coconut) before application.</p>
    </div>
    <div class="copy" style="top:145px;left:4px;right:4px;">
      <span class="rule"></span>
      <p class="heading">CAUTION:</p>
      <p style="margin-top:0;">Possible skin sensitivity. Keep out of reach of children. Not for ingestion or internal use. Avoid contact with eyes, inner ears and sensitive areas.</p>
    </div>
  </div>

  <div class="panel" style="left:232.5px;width:77.5px;">
    <div class="copy benefits" style="top:42px;left:4px;right:4px;">
      <span class="rule"></span>
      <p>Essential Oils have been used for centuries to help prepare the mind and body for sleep</p>
      <p>Dusk Haven contain a balanced blend of the most sleep supporting essential oils, renowned for their grounding and calming properties.</p>
      <p><b>Lavender</b><br>for restfulness<br><b>Vetiver</b><br>for grounding<br><b>Cedarwood</b><br>for relaxation<br><b>Marjoram</b><br>for balance<br><b>Roman Chamomile</b><br>for comfort</p>
      <p>Add Dusk Haven to your nightly bedtime ritual to help support you in achieving deep and rejuvenating sleep</p>
    </div>
    <p class="reverse reverse--small" style="left:2px;right:2px;top:309px;text-align:center;"><b>Visit</b><br>www.duskhaven.com.au<br>to learn more</p>
    <p class="reverse reverse--small" style="left:2px;right:2px;top:337px;text-align:center;">IG @duskhavenau</p>
  </div>

  <p class="reverse reverse--label" style="left:0;width:155px;top:313px;font-size:6.5px;">Made in Australia</p>
  <p class="reverse reverse--label" style="left:0;width:155px;top:335px;font-size:6.5px;">15mL</p>
</section>

</body>
</html>
```